Agricultural Consulting Website

Provide a modern yet business like website for my new Agriculture Consulting Business in Australia called FenTrove. Whilst we are based in Australia we are targetting both domestic and international markets (especially in Asia). We are targetting corporate, small business, government and farmer clients. The design should compliment our logo also sourced through pixel guild. The webiste should be easy for me to keep updated on a regular basis without the need to go back to the designer.

Industry/Entity Type

Business

Requirements
Must have
• clean crisp feel
• be modern yet business like
• be able to be updated by myself easily

```html
<!DOCTYPE html>
<html lang="en">
<head>
<meta charset="utf-8">
<title>FenTrove – Agricultural Consultancy</title>
<link href="https://fonts.googleapis.com/css2?family=Questrial&family=Open+Sans:wght@700&family=Arimo:wght@400&display=swap" rel="stylesheet">
<style>
:root{
  --page-green:#5f9400;
  --brand-green:#5e9a0e;
  --brand-brown:#6a3300;
  --button-brown:#5c2c00;
  --card-cream:#f4eed8;
  --panel-grey:#f2f2f2;
  --text-grey:#6b6b6b;
  --text-dark:#333;
  --white:#fff;
}
*{box-sizing:border-box;margin:0;padding:0}
html,body{width:1165px;height:1200px;overflow:hidden}
body{background:var(--page-green);font-family:"Arimo",Arial,sans-serif;position:relative}
.sheet{position:absolute;left:123px;top:28px;width:919px;height:1135px;background:var(--white)}
.brand{position:absolute;left:23px;top:24px;display:flex;align-items:center;gap:10px}
.brand-mark{width:64px;height:64px;background:var(--brand-brown)}
.brand-name{font-family:"Questrial",sans-serif;font-size:40px;color:var(--brand-green);letter-spacing:-0.5px}
.main-nav{position:absolute;right:22px;top:43px;display:flex;gap:4px}
.main-nav a{font-size:13px;color:var(--text-dark);text-decoration:none;padding:6px 16px;height:26px;line-height:14px}
.main-nav a.active{background:var(--brand-green);color:var(--white)}
.hero{position:absolute;left:23px;top:105px;width:874px;height:388px;
  background:linear-gradient(180deg,#bcd4e6 0%,#dfe7e4 12%,#8e9d4c 22%,#b3a84f 30%,#5f8f1b 42%,#3f7e0c 65%,#2f6b08 100%)}
.hero-title{position:absolute;left:0;right:0;top:198px;text-align:center;color:var(--white)}
.hero-title .line-one{display:block;font-family:"Questrial",sans-serif;font-size:44px;line-height:44px}
.hero-title .line-two{display:block;font-family:"Open Sans",sans-serif;font-weight:700;font-size:31px;line-height:34px}
.services{position:absolute;left:23px;top:518px;width:874px;height:270px}
.service{position:absolute;top:0;width:200px;height:270px;background:var(--card-cream);padding:0 13px}
.service h2{font-family:"Questrial",sans-serif;font-weight:400;font-size:19px;color:var(--brand-brown);margin-top:10px;height:31px;white-space:nowrap}
.service .thumb{width:179px;height:106px;border:2px solid var(--white)}
.service p{font-size:10.5px;line-height:14.5px;color:var(--text-grey);text-align:justify;margin-top:9px;letter-spacing:0.2px}
.service .more{position:absolute;left:15px;top:226px;background:var(--button-brown);color:var(--white);font-size:11px;width:75px;height:26px;line-height:26px;text-align:center;text-decoration:none}
.about{position:absolute;left:23px;top:828px;width:620px}
.about h1{font-family:"Questrial",sans-serif;font-weight:400;font-size:23px;color:var(--brand-brown)}
.about h1 .accent{color:var(--brand-green)}
.about p{font-size:12px;line-height:15.5px;color:var(--text-grey);margin-top:15px}
.about h1 + p{margin-top:17px}
.contact{position:absolute;left:696px;top:820px;width:201px;height:238px;background:var(--panel-grey);padding:10px 14px}
.contact h2{font-family:"Questrial",sans-serif;font-weight:400;font-size:20px;color:var(--brand-brown);padding-bottom:5px;border-bottom:1px solid #ccc}
.contact .lead{font-size:12.5px;line-height:15.5px;color:#000;text-align:justify;margin-top:10px}
.contact ul{list-style:none;margin-top:10px}
.contact li{display:flex;align-items:center;gap:10px;font-size:12.5px;color:var(--text-grey);height:28px}
.contact li svg{width:14px;height:14px;flex:none}
.social-badge{display:block;width:140px;height:43px;margin:8px 0 0 6px;background:var(--white);border:1px solid #d5d5d5}
.footer{position:absolute;left:23px;top:1087px;width:874px;border-top:1px solid #ccc;text-align:center;font-size:11px;color:var(--text-dark);padding-top:16px}
</style>
</head>
<body>
<div class="sheet">
  <header>
    <div class="brand"><span class="brand-mark"></span><span class="brand-name">FenTrove</span></div>
    <nav class="main-nav">
      <a href="#" class="active">Home</a>
      <a href="#">About us</a>
      <a href="#">Services</a>
      <a href="#">News &amp; Events</a>
      <a href="#">Contact us</a>
    </nav>
  </header>

  <section class="hero" role="img" aria-label="Rows of green crops stretching to rolling golden hills under a blue sky">
    <div class="hero-title"><span class="line-one">Your Farm Profit</span><span class="line-two">is Our Priority</span></div>
  </section>

  <section class="services">
    <article class="service" style="left:0">
      <h2>Farm Management</h2>
      <div class="thumb" role="img" aria-label="Round hay bales in a harvested field" style="background:linear-gradient(180deg,#4e7d2a 0%,#b99a5a 18%,#a8834a 60%,#8a6a3a 100%)"></div>
      <p>Lorem ipsum dolor sit amet, consectetur adipiscing elit. Morbi vitae justo malesuada, posuere erat sit amet, mollis lacus.</p>
      <a class="more" href="#">Read More</a>
    </article>
    <article class="service" style="left:223px">
      <h2>Grain Marketing</h2>
      <div class="thumb" role="img" aria-label="Close-up of golden wheat ears" style="background:linear-gradient(135deg,#e3b24a 0%,#c98a24 50%,#8d5a14 100%)"></div>
      <p>Lorem ipsum dolor sit amet, consectetur adipiscing elit. Morbi vitae justo malesuada, posuere erat sit amet, mollis lacus.</p>
      <a class="more" href="#">Read More</a>
    </article>
    <article class="service" style="left:449px">
      <h2>Agronomy</h2>
      <div class="thumb" role="img" aria-label="Crop rows in dark soil" style="background:linear-gradient(180deg,#9fb7c9 0%,#6c8a4a 10%,#3f6e22 45%,#3b3a22 100%)"></div>
      <p>Lorem ipsum dolor sit amet, consectetur adipiscing elit. Morbi vitae justo malesuada, posuere erat sit amet, mollis lacus.</p>
      <a class="more" href="#">Read More</a>
    </article>
    <article class="service" style="left:673px">
      <h2>Project Management</h2>
      <div class="thumb" role="img" aria-label="Two consultants reviewing notes in a green field" style="background:linear-gradient(180deg,#a7c3dc 0%,#8aa7a0 25%,#5f8a3a 55%,#3f6f22 100%)"></div>
      <p>Lorem ipsum dolor sit amet, consectetur adipiscing elit. Morbi vitae justo malesuada, posuere erat sit amet, mollis lacus.</p>
      <a class="more" href="#">Read More</a>
    </article>
  </section>

  <section class="about">
    <h1><span class="accent">FenTrove</span> Agricultural Consultancy</h1>
    <p>Lorem ipsum dolor sit amet, consectetur adipiscing elit. Morbi vitae justo malesuada, posuere erat sit amet, mollis lacus. Sed commodo ligula eget pretium dapibus. Suspendisse id nisi sed libero ultricies iaculis. Vestibulum turpis turpis, ultrices a eros ut, ullamcorper rhoncus tellus.</p>
    <p>Nulla eget consequat eros. Donec metus diam, mattis quis mattis elementum, eleifend sit amet est. Nunc scelerisque congue nulla, eu aliquam risus consectetur ac. Donec a accumsan felis. Proin nunc sem, ultricies ac diam a, ultrices tristique lorem. Pellentesque quis dapibus purus.</p>
    <p>Donec massa odio, porttitor molestie scelerisque et, pulvinar a odio. Pellentesque eros massa, ultricies in libero quis, feugiat ullamcorper risus.</p>
  </section>

  <aside class="contact">
    <h2>Contact us</h2>
    <p class="lead">Lorem ipsum dolor sit amet, consectetur adipiscing elit.</p>
    <ul>
      <li><svg viewBox="0 0 14 14"><path d="M3 1h3l1 3-2 1.5c.8 1.8 1.8 2.8 3.5 3.5L10 7l3 1v3c0 1-1 2-2 2C6 13 1 8 1 3c0-1 1-2 2-2z" fill="#6a3300"/></svg>1800 555 019</li>
      <li><svg viewBox="0 0 14 14"><rect x="1" y="3" width="12" height="8" fill="#6a3300"/><path d="M1 3l6 5 6-5" fill="none" stroke="#f2f2f2" stroke-width="1"/></svg>info@fentrove.com.au</li>
      <li><svg viewBox="0 0 14 14"><g fill="none" stroke="#8a5a2a" stroke-width="1"><circle cx="7" cy="7" r="5.5"/><ellipse cx="7" cy="7" rx="2.5" ry="5.5"/><path d="M1.5 7h11M2.5 4.5h9M2.5 9.5h9"/></g></svg>www.fentrove.com.au</li>
    </ul>
    <a class="social-badge" href="#" aria-label="Social page"></a>
  </aside>

  <footer class="footer">Copyright © 2013 FenTrove. All Rights Reserved.</footer>
</div>
</body>
</html>
```